Tranquil Pathway Business Card

Logo attached. (will be printing onto thick white/off white textured card)

Double sided business card for two Therapists working at Tranquil Pathway.

Require one design, but with different name and mobile numbers on each card.

Target Market(s)

Medical, Health

Industry/Entity Type

Business

Contact Information for Business Card

Need one business card design, but a separate card for each person - Colin Marchetti and Marieke de Boeckx.

FRONT OF CARD

Logo

Name (Colin Marchetti on one card, Marieke de Boeckx on the other)
Professional Clinical Hypnotherapist

Consulting Rooms (Near Lindqvist Hospital)
482 Brackenfield Road
Dunmore VIC 3987

Colin@TranquilPathway.example.au OR Marieke@TranquilPathway.example.au

Mobile: 0455 872 604 (for Colin) OR
Mobile: 0467 290 518 (for Marieke)

BACK OF CARD

Logo

Website: www.TranquilPathway.example.au

Phone: 1300 958 471

Requirements
Must have
• Text and logo only. No additiional graphics.

```html
<!DOCTYPE html>
<html lang="en">
<head>
<meta charset="utf-8">
<title>Tranquil Pathway Business Card</title>
<link rel="stylesheet" href="https://fonts.googleapis.com/css2?family=Ubuntu:wght@400;500;700&display=swap">
<style>
  :root {
    --navy: #232c5e;
    --grey-ring: #6a6a6a;
    --backdrop: #cccccc;
    --card-white: #ffffff;
    --ink: #1c1c1c;
    --rule: #333333;
    --swoosh-shadow: #c9c9c9;
  }
  * { margin: 0; padding: 0; box-sizing: border-box; }
  html, body { width: 1200px; height: 1000px; overflow: hidden; }
  body {
    background: var(--backdrop);
    position: relative;
    font-family: "Ubuntu", sans-serif;
  }
  .card {
    position: absolute;
    left: 226px;
    width: 747px;
    overflow: hidden;
  }
  .card-front {
    top: 66px;
    height: 432px;
    background: var(--card-white);
    box-shadow: 0 3px 0 #bdbdbd;
  }
  .card-back {
    top: 509px;
    height: 425px;
    background: var(--navy);
  }
  .front-swoosh { position: absolute; left: 0; top: 0; }
  .abs { position: absolute; }

  .front-name-banner {
    right: 28px; top: 28px;
    color: var(--card-white);
    font-weight: 700; font-size: 26px;
    white-space: nowrap;
  }

  .brand-mark {
    border-radius: 50%;
    background: var(--navy);
    border: 8px solid var(--grey-ring);
  }
  .brand-name {
    font-weight: 700;
    text-transform: uppercase;
    line-height: 1.05;
    white-space: nowrap;
  }
  .front-brand .brand-mark { left: 125px; top: 144px; width: 92px; height: 92px; }
  .front-brand .brand-name { left: 258px; top: 170px; font-size: 31px; color: var(--navy); }

  .person-name { left: 24px; top: 322px; font-size: 19px; font-weight: 700; color: var(--ink); white-space: nowrap; }
  .person-title { left: 23px; top: 350px; font-size: 12px; color: var(--ink); white-space: nowrap; }

  .column-rule { width: 4px; height: 83px; top: 302px; background: var(--rule); }
  .rule-one { left: 243px; }
  .rule-two { left: 486px; }

  .contact-lines {
    font-size: 10.5px; font-weight: 700; color: var(--ink);
    letter-spacing: -0.15px;
    white-space: nowrap;
  }
  .contact-lines p { height: 26.5px; }
  .address-lines { left: 265px; top: 318px; }
  .direct-lines { left: 507px; top: 323px; }
  .direct-lines p { height: 28px; }

  .back-brand .brand-mark { left: 189px; top: 82px; width: 106px; height: 106px; border-width: 9px; }
  .back-brand .brand-name { left: 330px; top: 104px; font-size: 33px; color: var(--card-white); }

  .back-contact {
    left: 121px; color: var(--card-white);
    font-weight: 700; font-size: 21px; white-space: nowrap;
  }
  .back-website { top: 236px; }
  .back-phone { top: 291px; }
</style>
</head>
<body>

<section class="card card-front">
  <svg class="front-swoosh" width="747" height="432" viewBox="0 0 747 432" aria-hidden="true">
    <path d="M0,0 H747 V290 C520,118 250,68 0,138 Z" fill="var(--swoosh-shadow)"/>
    <path d="M0,0 H747 V280 C520,108 250,60 0,131 Z" fill="var(--navy)"/>
    <path d="M0,124 C230,42 520,58 747,212" fill="none" stroke="var(--card-white)" stroke-width="5"/>
  </svg>

  <div class="abs front-name-banner">Marieke de Boeckx</div>

  <div class="front-brand">
    <div class="abs brand-mark"></div>
    <div class="abs brand-name">Tranquil<br>Pathway</div>
  </div>

  <div class="abs person-name">Marieke de Boeckx</div>
  <div class="abs person-title">Professional Clinical Hypnotherapist</div>

  <div class="abs column-rule rule-one"></div>
  <div class="abs contact-lines address-lines">
    <p>Consulting Rooms (Near Lindqvist Hospital)</p>
    <p>482 Brackenfield Road</p>
    <p>Dunmore VIC 3987</p>
  </div>

  <div class="abs column-rule rule-two"></div>
  <div class="abs contact-lines direct-lines">
    <p>Marieke@TranquilPathway.example.au</p>
    <p>Mobile: 0467 290 518</p>
  </div>
</section>

<section class="card card-back">
  <div class="back-brand">
    <div class="abs brand-mark"></div>
    <div class="abs brand-name">Tranquil<br>Pathway</div>
  </div>
  <div class="abs back-contact back-website">Website: www.TranquilPathway.example.au</div>
  <div class="abs back-contact back-phone">Phone: 1300 958 471</div>
</section>

</body>
</html>
```